Brightmoor Leisure Works Investor Brochure

Start Up Company Brightmoor Leisure Works requires 4 page A4 size brochure outlining and detailing new product. Draft layout attached. Information and points of difference included. Company logo and graphics attached. Final design should sell to investors.
Industry/Entity Type
It Company

```html
<!DOCTYPE html>
<html lang="en">
<head>
<meta charset="utf-8">
<title>Brightmoor Leisure Works – Investor Brochure Spread</title>
<link href="https://fonts.googleapis.com/css2?family=Arimo:wght@400;700&display=swap" rel="stylesheet">
<style>
  :root{
    --page-bg:#ece9e4;
    --slate:#5f5f61;
    --sky-panel:#7fa0d6;
    --banner:#4f86cf;
    --map-light:#6aa7f1;
    --map-navy:#0f2a6c;
    --paper:#f7f7f7;
    --paper-shade:#e6e6e6;
    --ink:#222;
    --bar:#3f6fb5;
    --bar-edge:#27508f;
    --rule:#4a7fcb;
    --alert:#e0241b;
    --white:#fff;
  }
  *{box-sizing:border-box;margin:0;padding:0}
  html,body{width:1200px;height:870px;overflow:hidden}
  body{background:var(--page-bg);font-family:"Arimo",Arial,sans-serif;color:var(--ink);position:relative}
  .spread{position:absolute;left:38px;top:36px;width:1124px;height:796px;background:var(--paper);box-shadow:0 2px 8px rgba(0,0,0,.25)}
  .panel{position:absolute}
  .panel--launch{left:0;top:0;width:562px;height:336px;background:var(--slate)}
  .panel--global{left:562px;top:0;width:562px;height:336px;background:var(--sky-panel)}
  .panel--stats{left:0;top:336px;width:562px;height:460px;background:linear-gradient(180deg,var(--paper-shade),var(--paper) 40%)}
  .panel--tech{left:562px;top:336px;width:562px;height:460px;background:linear-gradient(180deg,var(--paper-shade),var(--paper) 30%)}
  .banner{position:absolute;background:var(--banner);color:var(--white);font-weight:400;white-space:nowrap}
  .banner--title{height:28px;font-size:14.5px;line-height:28px;padding-left:9px;letter-spacing:-.1px;clip-path:polygon(0 0,100% 0,calc(100% - 22px) 100%,0 100%)}
  .banner--stat{height:47px;font-size:15.5px;line-height:21px;text-align:right;padding:3px 12px 0 0;clip-path:polygon(22px 0,100% 0,100% 100%,0 100%)}
  .launch-copy{position:absolute;left:12px;top:68px;width:190px;color:#f2f2f2;font-size:10.5px;line-height:22.4px;white-space:nowrap}
  .map{position:absolute}
  .map--australia{left:247px;top:50px;width:290px;height:275px;background:var(--map-light);border-radius:38% 42% 34% 40%}
  .map--world{left:50px;top:59px;width:490px;height:235px;background:var(--map-navy);border-radius:28%}
  .kiosk{position:absolute;left:4px;top:40px;width:234px;height:400px;background:linear-gradient(160deg,#6d9be0,#2f63b4 70%,#2c2c2c 96%);border-radius:6px 18px 4px 4px}
  .table-note{position:absolute;left:248px;top:165px;font-size:9px;white-space:nowrap}
  .airports{position:absolute;left:244px;top:180px;border-collapse:collapse;table-layout:fixed;width:301px;font-size:9.5px}
  .airports td{border:1px solid #333;height:19px;padding:0 5px;background:var(--white);white-space:nowrap;overflow:hidden}
  .airports .num{text-align:right;padding:0 4px}
  .chart-title{position:absolute;left:0;top:100px;width:562px;text-align:center;font-size:14px;font-weight:400;border-bottom:1.5px solid var(--rule);height:24px;line-height:18px}
  .chart{position:absolute;left:0;top:146px;width:562px;height:300px}
  .chart__axis{position:absolute;left:170px;top:-6px;width:1px;height:300px;background:#999}
  .chart__row{position:absolute;left:0;width:562px;height:14px}
  .chart__label{position:absolute;left:0;width:164px;text-align:right;font-size:6px;line-height:14px;color:#333;white-space:nowrap}
  .chart__bar{position:absolute;left:171px;top:0;height:13px;background:var(--bar);border-bottom:2px solid var(--bar-edge);border-right:2px solid var(--bar-edge)}
  .chart__note{position:absolute;font-size:6.5px;line-height:10px;color:#222;white-space:nowrap}
  .chart__note--alert{color:var(--alert)}
</style>
</head>
<body>
<main class="spread">
  <section class="panel panel--launch">
    <h2 class="banner banner--title" style="left:12px;top:14px;width:404px">COMING SOON TO AIRPORTS ACROSS AUSTRALIA</h2>
    <p class="launch-copy">Current technology allows up to<br>10,000 encrypted digital movies<br>to be stored on a kiosk.<br>Multiple customers can<br>simultaneously browse and rent<br>movies on the Kiosks FREE Wifi<br>Travellers are always killing time<br>waiting to board there flight.<br>Perfect time to browse movies.<br>Target of 1 million transactions in<br>the first 12 months</p>
    <div class="map map--australia" role="img" aria-label="Map of Australia marked with kiosk locations at airports"></div>
  </section>

  <section class="panel panel--global">
    <h2 class="banner banner--title" style="left:14px;top:14px;width:404px">TECHNOLOGY BUILT FOR GLOBAL EXPANSION</h2>
    <div class="map map--world" role="img" aria-label="World map"></div>
  </section>

  <section class="panel panel--stats">
    <div class="kiosk" role="img" aria-label="Brightmoor Leisure Works 'Flicks in Transit' movie download kiosk"></div>
    <p class="banner banner--stat" style="left:245px;top:21px;width:302px">145,000,000+ Passenger Movements<br>for YE Feb 2014. Up 3.1% on 2013</p>
    <p class="table-note">New Airport announced for Western Sydney to cope with increase demand.</p>
    <table class="airports">
      <colgroup><col style="width:94px"><col style="width:56px"><col style="width:84px"><col style="width:67px"></colgroup>
      <tr><td>SYDNEY</td><td class="num">38 437 737</td><td>MELBOURNE</td><td class="num">30 484 074</td></tr>
      <tr><td>BRISBANE</td><td class="num">21 570 625</td><td>PERTH</td><td class="num">12 989 955</td></tr>
      <tr><td>ADELAIDE</td><td class="num">7 460 471</td><td>GOLD COAST</td><td class="num">5 789 986</td></tr>
      <tr><td>CAIRNS</td><td class="num">4 293 485</td><td>CANBERRA</td><td class="num">2 931 006</td></tr>
      <tr><td>HOBART</td><td class="num">2 098 416</td><td>DARWIN</td><td class="num">2 023 665</td></tr>
      <tr><td>TOWNSVILLE</td><td class="num">1 543 457</td><td>LAUNCESTON</td><td class="num">1 267 589</td></tr>
      <tr><td>WILLIAMTOWN</td><td class="num">1 208 188</td><td>MACKAY</td><td class="num">1 083 805</td></tr>
      <tr><td>SUNSHINE COAST</td><td class="num">891 300</td><td>KARRATHA</td><td class="num">763 137</td></tr>
      <tr><td>ROCKHAMPTON</td><td class="num">694 368</td><td>ALICE SPRINGS</td><td class="num">667 383</td></tr>
      <tr><td>GLADSTONE</td><td class="num">500 429</td><td>PORT HEDLAND</td><td class="num">491 274</td></tr>
    </table>
  </section>

  <section class="panel panel--tech">
    <p class="banner banner--stat" style="left:248px;top:21px;width:300px">Top 20 Airports in the world exceeded<br>1.2 billion passengers in 2013</p>
    <h3 class="chart-title">Incorporating Blazing Fast Wifi</h3>
    <div class="chart" role="figure" aria-label="Connection speed comparison">
      <div class="chart__axis"></div>
      <div class="chart__row" style="top:0"><span class="chart__label">WiGig 802.11ad (2015) (7000 Mbps)</span><span class="chart__bar" style="width:330px"></span><span class="chart__note chart__note--alert" style="left:305px;top:-12px">Future Devices to Download SD Movies in a few seconds</span></div>
      <div class="chart__row" style="top:35px"><span class="chart__label">Wifi 802.11ac (1300 Mbps)</span><span class="chart__bar" style="width:62px"></span><span class="chart__note" style="left:245px;top:0">Corvane Tab S4 &amp; S5</span></div>
      <div class="chart__row" style="top:67px"><span class="chart__label">Wifi 802.11n (300 Mbps)</span><span class="chart__bar" style="width:21px"></span><span class="chart__note" style="left:200px;top:-3px">2013 Model Lumo Phone/Pad - Download SD Movies in Under 3 Minutes</span></div>
      <div class="chart__row" style="top:100px"><span class="chart__label">Wifi 802.11g (108 Mbps)</span><span class="chart__bar" style="width:8px"></span></div>
      <div class="chart__row" style="top:133px"><span class="chart__label">FibreNet 100 (100 Mbps)</span><span class="chart__bar" style="width:8px"></span></div>
      <div class="chart__row" style="top:167px"><span class="chart__label">FibreNet 50 (50 Mbps)</span><span class="chart__bar" style="width:6px"></span></div>
      <div class="chart__row" style="top:201px"><span class="chart__label">FibreNet 25 (25Mbps)</span><span class="chart__bar" style="width:5px"></span></div>
      <div class="chart__row" style="top:235px"><span class="chart__label">FibreNet 12 (12 Mbps)</span><span class="chart__bar" style="width:4px"></span></div>
      <div class="chart__row" style="top:270px"><span class="chart__label">ADSL 2+ (24Mbps)</span><span class="chart__bar" style="width:5px"></span></div>
    </div>
  </section>
</main>
</body>
</html>
```